Valdor Digworks LTD - website for irrigation & Landscape Lighting & Buried service wire

Looking for a website to help promote my business with Irrigation (installation, service, etc) and buried service wire/drainage solutions.

Commercial/Residential

Landscape lighting.

I’ll get photos in the trucks and trailers to upload as well maybe the machine as well.

Target Market(s)

Homeowners who want green grass and beautiful gardens. Beautiful landscape lighting

Industry/Entity Type

Irrigation systems and landscape lighting and buried service wire to homes and offering Drainage soltions.

Coding

Coded - Design and coding required

Number of Pages Required

4 page

Colors
F0912C
F2A743
F7CA91
FBE8D2
FDF5EE

Requirements
Must have
• was hoping to link up my email on valdordigworks@mailpost.example with the website if possible.
Nice to have
• Page for Irrigation, page for landscape lighting, page buried service wire & drainage soltions.

```html
<!DOCTYPE html>
<html lang="en">
<head>
<meta charset="utf-8">
<title>Valdor Digworks LTD</title>
<link href="https://fonts.googleapis.com/css2?family=Poppins:ital,wght@0,400;0,500;0,600;0,700;1,400&display=swap" rel="stylesheet">
<style>
:root{
  --orange:#f0912c;
  --orange-2:#f2a743;
  --orange-3:#f7ca91;
  --cream:#fbe8d2;
  --cream-2:#fdf5ee;
  --ink:#1a1a1a;
  --grey-text:#6b6b6b;
  --card-grey:#c4c4c4;
  --footer:#1e1e1e;
  --white:#ffffff;
}
*{margin:0;padding:0;box-sizing:border-box}
html,body{width:1200px;height:3349px;overflow:hidden}
body{font-family:"Poppins",sans-serif;color:var(--ink);background:var(--white);position:relative}
.abs{position:absolute}
.ph{position:absolute}

/* hero */
.hero{position:absolute;left:0;top:0;width:1200px;height:600px;
  background:radial-gradient(ellipse 340px 300px at 880px 250px,#f3c56a 0%,#c9822b 35%,transparent 70%),
  linear-gradient(180deg,#2a1a0c 0%,#3b2810 45%,#3f5a16 75%,#5d8a1d 100%)}
.brand{position:absolute;left:112px;top:60px;color:var(--orange);font-weight:600;font-size:22px;line-height:1.1;width:200px}
.brand small{display:block;font-size:22px}
.nav{position:absolute;top:72px;right:110px;display:flex;gap:33px}
.nav a{color:var(--white);text-decoration:none;font-size:13.5px;font-weight:500}
.hero h1{position:absolute;left:110px;top:232px;width:560px;color:var(--white);font-size:38px;font-weight:600;line-height:53px;text-align:justify}

/* offer */
.sec-title{position:absolute;left:0;width:1200px;text-align:center;color:var(--orange);font-size:39px;font-weight:600;letter-spacing:1px}
.intro{position:absolute;left:210px;top:734px;width:780px;text-align:center;color:var(--grey-text);font-size:16.5px;line-height:26px}
.card{position:absolute;top:848px;width:257px;height:322px;background:var(--card-grey)}
.card .ph{left:0;top:0;width:257px;height:222px}
.card .icon{position:absolute;left:82px;top:172px;width:94px;height:94px;border-radius:50%;background:var(--orange);display:flex;align-items:center;justify-content:center}
.card .label{position:absolute;left:0;width:257px;top:276px;text-align:center;font-size:21.5px;font-weight:600}
.arrow{position:absolute;top:938px;width:40px;height:40px;border-radius:50%;background:#111;display:flex;align-items:center;justify-content:center}

/* about */
.about-bg{left:0;top:1256px;width:1200px;height:512px;
  background:radial-gradient(ellipse 300px 200px at 950px 1000px,#c69a7a,transparent),linear-gradient(180deg,#8c9aa6 0%,#5f6a6e 50%,#4d5a3a 85%,#6f7048 100%)}
.about-box{position:absolute;left:112px;top:1340px;width:440px;height:262px;background:var(--white);padding:30px 30px}
.about-box h2{color:var(--orange);font-size:39px;font-weight:600;line-height:1;margin-bottom:18px}
.about-box p{color:var(--grey-text);font-size:16.5px;line-height:26px;text-align:justify}

/* testimonials */
.testi{position:absolute;left:0;top:1768px;width:1200px;height:498px;background:var(--orange-2)}
.t-card{position:absolute;background:var(--white);border-radius:22px;padding:26px 28px}
.t-card p{color:var(--grey-text);font-size:14.5px;line-height:22px;text-align:justify}
.t-card .who{position:absolute;left:27px;bottom:16px;display:flex;align-items:center;gap:18px}
.avatar{width:88px;height:88px;border-radius:50%;background:linear-gradient(135deg,#9a6b52,#4a3a35)}
.name{color:var(--orange);font-size:17px;font-weight:500;letter-spacing:.5px}
.role{font-size:14px;font-style:italic;color:#333}
.stars{position:absolute;right:28px;bottom:46px;display:flex;gap:2px}
.faded{opacity:.35;background:var(--orange-3)}
.dots{position:absolute;top:2165px;left:562px;display:flex;gap:9px}
.dots span{width:13px;height:13px;border-radius:50%;background:#111}
.dots span.on{background:var(--white)}

/* blog */
.post{position:absolute;top:2427px;width:298px}
.post .ph{left:0;top:0;width:298px;height:256px}
.post .cap{position:absolute;left:17px;top:208px;width:266px;background:var(--white);padding:8px 13px 0;font-size:17px;font-weight:500;line-height:23px;color:#333}
.post .more{position:absolute;left:30px;top:285px;color:var(--orange);font-size:14.5px;text-decoration:underline}
.btn{position:absolute;left:538px;top:2761px;width:126px;height:37px;border-radius:8px;background:var(--orange);color:#3a1f00;font-size:14px;display:flex;align-items:center;justify-content:center;box-shadow:0 3px 6px rgba(0,0,0,.2)}

/* footer */
.footer{position:absolute;left:0;top:2883px;width:1200px;height:466px;background:var(--footer);color:var(--white)}
.f-brand{position:absolute;left:112px;top:100px;font-size:24px;font-weight:600;line-height:1.15;color:var(--white)}
.f-col{position:absolute;top:84px}
.f-col h3{color:var(--orange);font-size:21px;font-weight:600;letter-spacing:.5px;margin-bottom:6px}
.f-col li{list-style:none;font-size:17.5px;line-height:34.5px;display:flex;align-items:center;gap:8px}
.rule{position:absolute;left:112px;width:978px;height:1px;background:#555}
.social{position:absolute;left:112px;top:327px;display:flex;gap:32px}
.social span{width:18px;height:18px;border:2px solid var(--white);border-radius:50%}
.f-nav{position:absolute;right:110px;top:323px;display:flex;gap:28px;font-size:17.5px}
.copy{position:absolute;left:0;width:1200px;top:412px;text-align:center;font-size:17.5px}
</style>
</head>
<body>

<header class="hero" role="img" aria-label="Glowing garden lamp among green leaves at dusk">
  <div class="brand">VALDOR<small>DIGWORKS LTD</small></div>
  <nav class="nav">
    <a>HOME</a><a>IRRIGATION INSTALLS</a><a>SERVICE</a><a>LANDSCAPE LIGHTING</a><a>FIBER OPTIC INSTALLATION</a>
  </nav>
  <h1>Homeowners who want green grass and beautiful gardens. Beautiful landscape lighting</h1>
</header>

<h2 class="sec-title" style="top:674px">WHAT WE OFFER</h2>
<p class="intro">Lorem ipsum dolor sit amet, consectetur adipiscing elit, sed do eiusmod tempor incididunt ut labore et dolore magna aliqua. Quis ipsum suspendisse ultrices gravida. Risus commodo viverra maecenas accumsan lacus vel facilisis.</p>

<div class="arrow" style="left:113px"><svg width="14" height="14" viewBox="0 0 14 14"><path d="M9 2 L4 7 L9 12" stroke="#fff" stroke-width="2.2" fill="none"/></svg></div>
<div class="arrow" style="left:1047px"><svg width="14" height="14" viewBox="0 0 14 14"><path d="M5 2 L10 7 L5 12" stroke="#fff" stroke-width="2.2" fill="none"/></svg></div>

<div class="card" style="left:178px">
  <div class="ph" role="img" aria-label="Garden bollard light on a lawn at evening" style="background:linear-gradient(180deg,#2e3a1e,#4f7a2a 60%,#6a8d3a)"></div>
  <div class="icon"><svg width="44" height="44" viewBox="0 0 44 44" fill="none" stroke="#fff" stroke-width="2"><rect x="17" y="6" width="10" height="10"/><line x1="22" y1="16" x2="22" y2="34"/><path d="M6 38 L10 30 L14 38 M18 38 L22 30 L26 38 M30 38 L34 30 L38 38"/><line x1="4" y1="38" x2="40" y2="38"/></svg></div>
  <div class="label">Residential</div>
</div>
<div class="card" style="left:472px">
  <div class="ph" role="img" aria-label="Office towers with landscaped plaza and lamp posts" style="background:linear-gradient(180deg,#7aa0c8,#486b8a 55%,#5a7a48)"></div>
  <div class="icon"><svg width="44" height="44" viewBox="0 0 44 44" fill="none" stroke="#fff" stroke-width="2"><path d="M14 24 L26 12 L32 18 L20 30 Z"/><line x1="20" y1="30" x2="20" y2="38"/><rect x="14" y="36" width="12" height="4"/><path d="M30 8 L32 4 M35 11 L39 9 M34 15 L38 16"/></svg></div>
  <div class="label">Commercial</div>
</div>
<div class="card" style="left:766px">
  <div class="ph" role="img" aria-label="Technician in hard hat installing cable at a wall" style="background:linear-gradient(180deg,#b9b5ad,#9c9890 60%,#6f7a8a)"></div>
  <div class="icon"><svg width="44" height="44" viewBox="0 0 44 44" fill="none" stroke="#fff" stroke-width="2"><path d="M6 10 C18 14 22 24 30 34 M6 18 C16 20 22 28 28 38 M12 6 C22 12 28 20 36 28 M20 6 C28 12 34 18 40 22"/></svg></div>
  <div class="label">Fiber Optic installation</div>
</div>

<div class="ph about-bg" role="img" aria-label="Modern house with lit windows and lawn lights at dusk"></div>
<div class="about-box">
  <h2>ABOUT US</h2>
  <p>Lorem ipsum dolor sit amet, consectetur adipiscing elit, sed do eiusmod tempor incididunt ut labore et dolore magna aliqua. Quis ipsum suspendisse ultrices gravida. Risus commodo viverra maecenas accumsan lacus</p>
</div>

<section class="testi">
  <h2 class="sec-title" style="top:74px;color:var(--white)">SEE WHAT THEY ARE SAYING</h2>
  <div class="t-card faded" style="left:-120px;top:182px;width:372px;height:195px"></div>
  <div class="t-card faded" style="left:948px;top:182px;width:372px;height:195px"></div>
  <div class="t-card" style="left:309px;top:166px;width:581px;height:194px">
    <p>Lorem ipsum dolor sit amet, consectetur adipiscing elit, sed do eiusmod tempor incididunt ut labore et dolore magna aliqua. Quis ipsum suspendisse ultrices gravida.</p>
    <div class="who">
      <div class="avatar" role="img" aria-label="Customer portrait"></div>
      <div><div class="name">MARLON REYES</div><div class="role">CEO Company</div></div>
    </div>
    <div class="stars">
      <svg width="108" height="20" viewBox="0 0 108 20" fill="var(--orange)"><g id="s"><path d="M10 1 L12.6 7 L19 7.4 L14 11.6 L15.6 18 L10 14.5 L4.4 18 L6 11.6 L1 7.4 L7.4 7 Z"/></g><use href="#s" x="22"/><use href="#s" x="44"/><use href="#s" x="66"/><use href="#s" x="88"/></svg>
    </div>
  </div>
  <div class="dots" style="top:397px"><span></span><span class="on"></span><span></span><span></span></div>
</section>

<h2 class="sec-title" style="top:2340px">OUR BLOG</h2>
<div class="post" style="left:110px">
  <div class="ph" role="img" aria-label="Man reading a document in a kitchen" style="background:linear-gradient(135deg,#3d3a38,#6a625c)"></div>
  <div class="cap">Lorem ipsum dolor sit amet, consect</div>
  <a class="more">LEARN MORE</a>
</div>
<div class="post" style="left:451px">
  <div class="ph" role="img" aria-label="Rock garden lit by landscape lights at night" style="background:radial-gradient(circle at 70% 40%,#d9b06a,#4a4860 60%,#2a2c3a)"></div>
  <div class="cap">Lorem ipsum dolor sit amet, consect</div>
  <a class="more">LEARN MORE</a>
</div>
<div class="post" style="left:792px">
  <div class="ph" role="img" aria-label="Apartment buildings with lit walkway at dusk" style="background:linear-gradient(180deg,#4f6fb0,#8a7a6a 60%,#4c4a30)"></div>
  <div class="cap">Lorem ipsum dolor sit amet, consect</div>
  <a class="more">LEARN MORE</a>
</div>
<div class="btn">VIEW MORE</div>

<footer class="footer">
  <div class="f-brand">VALDOR<br>DIGWORKS LTD</div>
  <div class="f-col" style="left:351px"><h3>SERVICES</h3><ul><li>Commercial</li><li>Residential</li><li>Landscape lighting</li><li>Fiber Optic installation</li></ul></div>
  <div class="f-col" style="left:608px"><h3>RESOURCES</h3><ul><li>Contact</li><li>Blog</li><li>Info</li><li>Account</li></ul></div>
  <div class="f-col" style="left:815px"><h3>COMPANY DETAILS</h3><ul>
    <li><svg width="14" height="18" viewBox="0 0 14 18" fill="#fff"><path d="M7 0 C3 0 0 3 0 7 C0 12 7 18 7 18 C7 18 14 12 14 7 C14 3 11 0 7 0 Z M7 9.5 A2.5 2.5 0 1 1 7 4.5 A2.5 2.5 0 1 1 7 9.5 Z"/></svg>Lorem ipsum dolor</li>
    <li><svg width="16" height="16" viewBox="0 0 16 16" fill="#fff"><path d="M3 0 L6 4 L4.5 6 C5.5 8 8 10.5 10 11.5 L12 10 L16 13 L14 16 C7 16 0 9 0 2 Z"/></svg>+1 888 8888 8888</li>
    <li><svg width="16" height="12" viewBox="0 0 16 12" fill="#fff"><path d="M0 0 H16 V12 H0 Z M1 1 L8 7 L15 1" stroke="#1e1e1e" stroke-width="1.2"/></svg>valdordigworks@mailpost.example</li>
  </ul></div>
  <div class="rule" style="top:294px"></div>
  <div class="social" aria-label="Social links"><span></span><span></span><span></span><span></span></div>
  <div class="f-nav"><span>Home</span><span>Irrigation Installs</span><span>Service</span><span>Landscape Lighting</span><span>Fiber Optic Installation</span></div>
  <div class="rule" style="top:380px"></div>
  <div class="copy">2024 Valdor Digworks Ltd. All Rights Reserved.</div>
</footer>

</body>
</html>
```